We are creating the packaging for our premium gift box: “Sunward Links Reserve.”
This box contains a green fee for two people, valid at the recipient’s choice of one of the most exclusive and scenic golf courses in Italy.
• Box dimensions: 16x16 x 2 cm
• Label coverage: The design must wrap around the two large square sides and the two lateral edges, similar to Gleamcase packaging.
• Style: Elegant, refined, and modern.

Front design:
• A strong emotional golf image (luxury golf course setting, Italian landscape, or moment of play).
• Title: “Sunward Links Reserve”.
• It must be clearly visible that the box includes a round of golf for two people in one of the 50 most exclusive and scenic golf courses in Italy.

Back design:
The back should contain the following text:

Discover Italy’s most iconic golf courses
With this gift box you and a guest can enjoy a round of golf at your choice of one of the 20 most beautiful courses in Italy. From championship layouts to breathtaking landscapes, every round is an unforgettable experience.

Some of the included courses:
• Tessa Varnelli Golf Club, Rome (host of the Halvern Trophy 2023)
• Grand Bosco Le Fontane, Turin
• Calmora Resort, Sicily
• Circolo Golf Villa Brunetta, Lake Como
• Lunaro Golf Club, Costa Smeralda
• Belvedrano Golf Club, Tuscany
• Golf Club Montefrassino, Piedmont

…and many more top-ranked Italian destinations.

How it works:
1. Choose your preferred golf course from the list.
2. Book directly with the club, using the code provided inside the box.
3. Enjoy an exclusive round of golf for two people.

This gift box offers flexibility, freedom, and access to Sunward Links Reserve experiences — the perfect present for any passionate golfer.

The overall design should capture the prestige of Italian golf and communicate that this is the most desired gift for golf lovers.

Target Market(s)

Our target market is golf enthusiasts, gift buyers, and people looking for premium experience gifts. The typical buyer is between 30–60 years old, often purchasing for friends, family, or business partners. The gift should feel aspirational, elegant, and special — the perfect present for any golfer.

Industry/Entity Type

Gift boxes and experience packages, with a specific focus on golf and premium leisure experiences.

Font styles to use
Serif

Requirements
Must have
• A premium, elegant box design (21x21x2 cm) in line with luxury gift standards. • Emotional, high-quality golf imagery that immediately conveys the excitement of playing golf. • Clear and stylish branding of TeeParcel. • A design style inspired by Gleamcase (label wrapping front + two sides + back). • On the back: a list of included golf courses and simple instructions on how to use the gift box.
Nice to have
• Minimalist and modern style with clean lines. • Touches of copper or metallic accents for a premium feel. • A contemporary design aesthetic similar to Nook Drive or Parvenda. • Lifestyle imagery that conveys joy, elegance, and aspiration, not just golf action.
Should not have
• No cheap or cluttered visuals. • No heavy use of gold or champagne tones (avoid cliché luxury). • No cartoonish or overly playful styles. • No complex text-heavy design — clarity and elegance are key.

```html
<!DOCTYPE html>
<html lang="en">
<head>
<meta charset="utf-8">
<title>Sunward Links Reserve – Box Label Dieline</title>
<link rel="stylesheet" href="https://fonts.googleapis.com/css2?family=EB+Garamond:wght@400;500&family=Libre+Baskerville:wght@400;700&display=swap">
<style>
  :root {
    --canvas: #ebebeb;
    --olive: #737b45;
    --olive-dark: #5f6736;
    --ivory: #f6f3ea;
    --accent-gold: #dcb446;
    --photo-sky: #d9a640;
    --photo-trees: #4f5a26;
    --photo-grass: #8fae3a;
  }
  * { margin: 0; padding: 0; box-sizing: border-box; }
  html, body { width: 1200px; height: 849px; overflow: hidden; }
  body {
    background: var(--canvas);
    font-family: "EB Garamond", Georgia, serif;
    color: var(--ivory);
    position: relative;
  }
  .dieline { position: absolute; left: 0; top: 0; }
  .dieline .panel { fill: var(--olive); }

  .front-photo {
    position: absolute;
    left: 436.5px; top: 74.5px; width: 327px; height: 324px;
    background:
      radial-gradient(ellipse at 78% 10%, rgba(245,200,90,.85), rgba(245,200,90,0) 45%),
      linear-gradient(180deg, var(--photo-sky) 0%, var(--photo-trees) 40%, #5e7a2a 56%, var(--photo-grass) 100%);
  }

  .front-title {
    position: absolute; left: 471px; top: 311px;
    font-size: 15px; font-weight: 400; letter-spacing: .2px;
    white-space: nowrap;
  }
  .offer-frame {
    position: absolute; left: 468.5px; top: 333px; width: 129px; height: 39px;
    border: 0.6px solid var(--ivory);
    font-family: "Libre Baskerville", Georgia, serif;
  }
  .offer-frame .offer-head {
    height: 10px; border-bottom: 0.6px solid var(--ivory);
    font-size: 4.2px; letter-spacing: .3px; text-align: center; line-height: 10px;
  }
  .offer-frame .offer-row { display: flex; height: 28px; }
  .offer-frame .people {
    width: 29px; border-right: 0.6px solid var(--ivory);
    text-align: center; padding-top: 2px;
  }
  .offer-frame .people b { display: block; font-size: 13px; font-weight: 400; line-height: 13px; }
  .offer-frame .people span { font-size: 4px; letter-spacing: .3px; }
  .offer-frame .courses { display: flex; align-items: center; padding-left: 4px; gap: 3px; }
  .offer-frame .courses b { font-size: 20px; font-weight: 400; }
  .offer-frame .courses span { font-size: 3.9px; line-height: 4.6px; letter-spacing: .2px; }

  .flap-title {
    position: absolute; left: 373.5px; width: 451.5px;
    text-align: center; font-size: 14px; letter-spacing: .3px;
  }
  .flap-title.top { top: 411px; }
  .flap-title.bottom { top: 782px; transform: rotate(180deg); }

  .back-copy {
    position: absolute; left: 352.5px; top: 445.5px; width: 495px; height: 326px;
    transform: rotate(180deg);
    text-align: center; padding-top: 48px;
  }
  .back-copy h2 {
    font-weight: 400; font-size: 11px; color: var(--accent-gold); letter-spacing: .3px;
    margin-bottom: 4px;
  }
  .back-copy p { font-size: 6.6px; line-height: 9.5px; }
  .back-copy .intro { margin-bottom: 28px; }
  .course-list {
    display: grid; grid-template-columns: 1fr 1fr; gap: 0 30px;
    list-style: none; width: 340px; margin: 4px auto 6px; text-align: left;
    font-size: 6.6px; line-height: 9.5px;
  }
  .course-list li { padding-left: 10px; position: relative; }
  .course-list li::before {
    content: ""; position: absolute; left: 0; top: 3.5px;
    width: 2.5px; height: 2.5px; border-radius: 50%; background: var(--accent-gold);
  }
  .back-copy .more { margin-bottom: 28px; }
  .steps { list-style: none; font-size: 6.6px; line-height: 9.5px; margin-bottom: 6px; }
  .back-copy .closing { font-size: 4.6px; line-height: 7px; }
</style>
</head>
<body>
  <svg class="dieline" width="1200" height="849" viewBox="0 0 1200 849" aria-hidden="true">
    <path class="panel" d="M436.5 398.5 V75 Q436.5 37 474.5 37 H725.5 Q763.5 37 763.5 75 V398.5 Z"/>
    <polygon class="panel" points="373.5,402 825,402 825,430 800,432 800,439.5 400,439.5 400,432 373.5,430"/>
    <polygon class="panel" points="352.5,445.5 400,445.5 400,451 847.5,451 847.5,445.5 847.5,771.5 800,771.5 800,766 352.5,766 352.5,771.5 352.5,445.5"/>
    <polygon class="panel" points="400,775.5 800,775.5 800,783 825,785 825,809 373.5,809 373.5,785 400,783"/>
  </svg>

  <div class="front-photo" role="img" aria-label="Smiling golfer holding a driver on a sunlit Italian golf green with a flag and tree line at golden hour"></div>

  <h1 class="front-title">Sunward Links Reserve</h1>
  <div class="offer-frame">
    <div class="offer-head">THE BOX INCLUDES A ROUND OF GOLF</div>
    <div class="offer-row">
      <div class="people"><b>2</b><span>PEOPLE</span></div>
      <div class="courses"><b>50</b><span>MOST EXCLUSIVE<br>AND SCENIC GOLF<br>COURSES IN ITALY.</span></div>
    </div>
  </div>

  <div class="flap-title top">Sunward Links Reserve</div>

  <section class="back-copy">
    <h2>Discover Italy’s Most Iconic Golf Courses</h2>
    <p class="intro">With this gift box you and a guest can enjoy a round of golf<br>at your choice of one of the 20 most beautiful courses in Italy.<br>From championship layouts to breathtaking landscapes,<br>every round is an unforgettable experience.</p>

    <h2>Some Of The Included Courses</h2>
    <ul class="course-list">
      <li>Tessa Varnelli Golf Club, Rome<br>(host of the Halvern Trophy 2023)</li>
      <li>Circolo Golf Villa Brunetta, Lake Como</li>
      <li>Grand Bosco Le Fontane, Turin</li>
      <li>Lunaro Golf Club, Costa Smeralda</li>
      <li>Calmora Resort, Sicily</li>
      <li>Belvedrano Golf Club, Tuscany</li>
      <li></li>
      <li>Golf Club Montefrassino, Piedmont</li>
    </ul>
    <p class="more">…and many more top-ranked Italian destinations.</p>

    <h2>How It Works</h2>
    <ol class="steps">
      <li>1. Choose your preferred golf course from the list.</li>
      <li>2. Book directly with the club, using the code provided inside the box.</li>
      <li>3. Enjoy an exclusive round of golf for two people.</li>
    </ol>
    <p class="closing">This gift box offers flexibility, freedom, and access to Sunward Links Reserve experiences<br>— the perfect present for any passionate golfer.</p>
  </section>

  <div class="flap-title bottom">Sunward Links Reserve</div>
</body>
</html>
```